Dutch craft distillery needs labels designed for Gin bottle

We are a small craft distillery based in The Netherlands. We are currently producing only GIN. While we do have a logo for our distillery, we are still in search of a winning design for our Gin bottle. We are looking for something modern yet classy. Let your creativity run wild. Play around with colours, think out of the box….The winning designer will be challenged to create the coolest labels for the different flavours of Gin we will be producing in the near future. The label will maintain the same design elements throughout the design, but will also be able to differentiate each variety clearly. So for e.g. A flowery Vantoor Gin can have a pink label with a different description and a spicy Vantoor gin can have another colour with another description and so on. If the design really appeals to us, we might also invite the designer to do our website for us!

In a nutshell: It is a 500 ml bottle, (Please check the attachment so you get an idea as to what kind of bottle to imagine while making the labels). The bottle is going to have a light coloured wooden lid/cork to it. As of now we have a transparent seal to complete the sealing process once the bottling is done. The idea is that we will have two labels. One in the front and one behind. The size of the labels are as follows:

Front label: 102 x 76 mm the front label. (TO BE USED HORIZONTALLY). The details that we need on the front label are in a separate attachment.

Back label: The size for the label at the back of the bottle is: 76 x 51 mm (TO BE USED VERTICALLY) The information that needs to come on the label behind is also in the same document which is attached separately. The label behind will also have batch no. & date (Please refer to attachment to understand what I mean by batch no. date, distiller’s signature etc.) I have attached a picture of an already existing brand which has its batch number and distillers signature etc on it….so you can understand what I exactly mean by that. Please do not copy their design, this is purely to give you an idea as to what I mean by batch number and so on. The address of the distillery can be put horizontally, vertically, on the side along one border, or however you find appropriate. This is the address:
Klaverhoekstraat 41,
6318 KT, Hengelo.
The Netherlands.
www.vantoor.nl

Logo’s no drinking when pregnant, No driving and drinking, No drinking under the age of 18 need to be present on the label behind. Alternately, we can also have www.calm-sipping.com instead of the under 18 no alcohol sign, most alcohol bottles these days have it. Please let me know what else you would need from me for this. So be creative and do your best!

Thanks and regards, Marisol Vendekampa.

Target Market(s)

Largely males and females between 25-55 , the audience could even be slightly older.

Colors

Designer to choose colors to be used in the design.

Requirements
Must have
• 1) The labels need to be modern, yet classy, elite..
• 2) We need to specify the fact that we are a craft distillery and the gin is HANDMADE, using only the highest quality ingredients.
• 3) We at Vantoor live, breathe, dream, talk about our dream which is our distillery and its product. The label needs to bring home this point and should clearly specify and mention that it is produced and bottled in The Netherlands. Or handmade and bottled with love and passion in The Netherlands or something to that effect if it matches with the rest of the design.
• 4) The colours you chose must match in some way or the other with the colours used for the logo design.
Nice to have
• Would be nice to have colours and look bold, although not completely necessary.
Should not have
• What I definitely do not want is something too whacky like a skull or some kind of vague work of art. For the rest, I leave it upto you….!

```html
<!DOCTYPE html>
<html lang="en">
<head>
<meta charset="utf-8">
<title>Vantoor Gin – Label Variations</title>
<link rel="stylesheet" href="https://fonts.googleapis.com/css2?family=Rye&family=Oswald:wght@400;500;600&family=Josefin+Sans:wght@400;700&family=Pinyon+Script&family=Old+Standard+TT:wght@400;700&family=Cinzel:wght@700&display=swap">
<style>
  :root{
    --backdrop:#3a2a1f;
    --paper:#f1f1ef;
    --teal-deep:#17877a;
    --teal-bright:#2bb1a9;
    --teal-band:#1fc2b8;
    --peach:#f4a977;
    --ink:#1e1b38;
    --charcoal:#4a4646;
    --royal:#1d4f9f;
    --orange:#ee8a45;
    --logo-red:#ec5532;
    --frame-blue:#1f6f92;
    --teal-dark:#0f6b66;
    --navy-border:#1b1530;
    --cream:#efe9dc;
    --wine:#4a1230;
    --wine-band:#300a1d;
    --rose:#c84f7c;
    --ornament:#8a8394;
  }
  *{margin:0;padding:0;box-sizing:border-box}
  html,body{width:1200px;height:900px;overflow:hidden;background:var(--backdrop)}
  .board{position:relative;width:1200px;height:900px}
  .label{position:absolute;width:542px;height:410px;overflow:hidden}
  .label--classic{left:28px;top:30px;background:var(--paper);color:var(--ink)}
  .label--split{left:30px;top:460px;background:linear-gradient(90deg,var(--teal-bright) 50%,var(--peach) 50%);color:var(--ink)}
  .label--diagonal{left:628px;top:30px;background:var(--navy-border)}
  .label--wine{left:628px;top:475px;height:400px;overflow:visible}

  .frame{position:absolute;inset:0;width:100%;height:100%}
  .center{position:absolute;left:0;right:0;text-align:center}

  .claim{position:absolute;top:66px;font:400 11px "Old Standard TT",serif}
  .claim--left{left:80px}.claim--right{right:80px}
  .maker-name{top:46px;font:600 30px "Oswald",sans-serif;letter-spacing:2px;color:var(--logo-red)}
  .gin-name{top:126px;font:400 70px/1 "Rye",serif;letter-spacing:1px}
  .label--classic .gin-name{color:var(--teal-deep)}
  .gin-word{top:200px;font:400 40px/1 "Rye",serif;color:var(--charcoal)}
  .gin-word::before,.gin-word::after{content:"";display:inline-block;width:64px;height:8px;background:currentColor;vertical-align:middle;margin:0 14px}
  .gin-word::before{clip-path:polygon(0 40%,100% 0,100% 100%,0 60%)}
  .gin-word::after{clip-path:polygon(0 0,100% 40%,100% 60%,0 100%)}
  .premium{top:240px;font:600 11px "Oswald",sans-serif;letter-spacing:2px;color:var(--royal)}
  .premium-rule{position:absolute;top:256px;left:150px;right:150px;height:1px;background:var(--royal)}
  .makers-line{top:262px;font:400 18px "Pinyon Script",cursive}
  .style-name{top:288px;font:400 26px "Rye",serif;color:var(--orange);letter-spacing:1px}
  .batch{top:318px;font:500 8px "Oswald",sans-serif;letter-spacing:1px}
  .batch span{padding:0 8px;position:relative}
  .batch span::before,.batch span::after{content:"";position:absolute;top:50%;width:70px;height:1px;background:currentColor}
  .batch span::before{right:100%}.batch span::after{left:100%}
  .facts{position:absolute;top:348px;left:140px;right:140px;display:flex;justify-content:space-between;align-items:center;font:400 11px "Old Standard TT",serif;border-top:1px solid currentColor;border-bottom:1px solid currentColor;padding:2px 0}
  .origin-oval{font-size:8px;line-height:1.05;text-align:center;border:1px solid currentColor;border-radius:50%;padding:4px 10px;background:var(--paper)}

  .label--split .gin-name{color:var(--ink);top:136px}
  .label--split .gin-word{color:var(--ink);top:200px}
  .label--split .premium{top:243px;color:var(--ink);font-weight:400;font-size:10px}
  .label--split .makers-line{top:260px;font:400 11px "Old Standard TT",serif;letter-spacing:1px}
  .label--split .style-name{top:276px;font:700 26px "Cinzel",serif;color:var(--ink)}
  .label--split .batch{top:310px}
  .label--split .facts{top:332px}
  .label--split .premium-rule{display:none}

  .diagonal-field{position:absolute;left:12px;top:12px;right:12px;bottom:12px}
  .badge{position:absolute;left:101px;width:340px;height:220px}
  .label--diagonal .badge{top:30px}
  .label--wine .badge{left:107px;top:0}
  .style-caps{font:700 33px "Josefin Sans",sans-serif;letter-spacing:1px}
  .label--diagonal .style-caps{top:252px;color:var(--ink)}
  .info-band{position:absolute;left:12px;right:12px;font:400 12.5px/1.3 "Josefin Sans",sans-serif;letter-spacing:.6px;text-align:center;padding:5px 0}
  .label--diagonal .info-band{top:292px;background:var(--teal-band);color:var(--ink);font-weight:700;border-top:1px solid var(--ink);border-bottom:1px solid var(--ink)}
  .fact-row{position:absolute;display:flex;justify-content:space-between}
  .label--diagonal .fact-row{top:348px;left:30px;right:30px;font:400 20px "Oswald",sans-serif;color:var(--ink);letter-spacing:-.3px}
  .label--wine .style-caps{top:236px;color:var(--cream);font-size:31px}
  .label--wine .info-band{top:282px;left:24px;right:24px;background:var(--wine-band);color:#fff;border-top:1px solid #c9a2b4;border-bottom:1px solid #c9a2b4}
  .label--wine .fact-row{top:340px;left:38px;right:30px;font:400 15px "Josefin Sans",sans-serif;color:#d8c2cc}
</style>
</head>
<body>
<main class="board">

  <section class="label label--classic">
    <svg class="frame" viewBox="0 0 542 410" fill="none" stroke="var(--frame-blue)">
      <defs>
        <g id="corner-classic">
          <path d="M14 120 V14 H170" stroke-width="3"/>
          <path d="M24 110 V40 Q24 24 40 24 H160" stroke-width="1.2"/>
          <path d="M38 100 V62 Q38 38 62 38 H150" stroke-width="1"/>
        </g>
      </defs>
      <use href="#corner-classic"/>
      <use href="#corner-classic" transform="translate(542 0) scale(-1 1)"/>
      <use href="#corner-classic" transform="translate(0 410) scale(1 -1)"/>
      <use href="#corner-classic" transform="translate(542 410) scale(-1 -1)"/>
      <path d="M14 160 V260 M24 170 V250 M528 160 V260 M518 170 V250" stroke-width="1.5"/>
      <path d="M72 80 H210 M332 80 H470" stroke="var(--ink)" stroke-width=".8"/>
    </svg>
    <p class="claim claim--left">100% Natural Botanicals</p>
    <p class="claim claim--right">No Artificial Flavouring</p>
    <p class="center maker-name">VANTOOR</p>
    <h1 class="center gin-name">VANTOOR</h1>
    <p class="center gin-word">GIN</p>
    <p class="center premium">PREMIUM</p>
    <div class="premium-rule"></div>
    <p class="center makers-line">Distilled And Bottled By Vantoor Distillery</p>
    <p class="center style-name">LONDON DRY GIN</p>
    <p class="center batch"><span>HANDCRAFTED IN SMALL BATCH</span></p>
    <div class="facts"><span>50 CL|43% ALC.</span><span class="origin-oval">PRODUCT OF<br>NETHERLANDS</span><span>VOL. 500 ML</span></div>
  </section>

  <section class="label label--diagonal">
    <svg class="diagonal-field" viewBox="0 0 518 386" preserveAspectRatio="none">
      <defs>
        <radialGradient id="purple-glow" cx="0.7" cy="0" r="0.9">
          <stop offset="0" stop-color="#b52fb8"/><stop offset="1" stop-color="#5a1566"/>
        </radialGradient>
        <radialGradient id="teal-glow" cx="0.5" cy="0.3" r="0.8">
          <stop offset="0" stop-color="#1fa39b"/><stop offset="1" stop-color="var(--teal-dark)"/>
        </radialGradient>
      </defs>
      <rect width="518" height="386" fill="url(#teal-glow)"/>
      <polygon points="0,0 518,0 518,40 0,200" fill="url(#purple-glow)"/>
      <polygon points="0,200 518,40 518,62 0,226" fill="var(--navy-border)"/>
    </svg>
    <svg class="badge" viewBox="0 0 340 220" aria-label="Vantoor Gin premium badge">
      <use href="#badge-art"/>
    </svg>
    <p class="center style-caps">LONDON DRY GIN</p>
    <p class="info-band">100% NATURAL BOTANICALS &#9679; NO ARTIFICIAL FLAVOURING<br>DISTILLED AND BOTTLED BY VANTOOR DISTILLERY</p>
    <div class="fact-row"><span>50 CL|43% ALC.</span><span>PRODUCT OF NETHERLANDS</span><span>VOL. 500 ML</span></div>
  </section>

  <section class="label label--split">
    <svg class="frame" viewBox="0 0 542 410" fill="none" stroke="var(--ink)">
      <rect x="12" y="12" width="518" height="386" stroke-width="2"/>
      <rect x="20" y="20" width="502" height="370" stroke-width="1"/>
      <defs>
        <g id="corner-split">
          <path d="M34 110 V46 Q34 34 46 34 H140" stroke-width="3"/>
          <path d="M46 100 V60 Q46 46 60 46 H130" stroke-width="1"/>
        </g>
      </defs>
      <use href="#corner-split"/>
      <use href="#corner-split" transform="translate(542 0) scale(-1 1)"/>
      <use href="#corner-split" transform="translate(0 410) scale(1 -1)"/>
      <use href="#corner-split" transform="translate(542 410) scale(-1 -1)"/>
      <path d="M34 170 V250 M508 170 V250" stroke-width="2"/>
      <path d="M72 82 H210 M332 82 H470" stroke-width=".8"/>
    </svg>
    <p class="claim claim--left">100% Natural Botanicals</p>
    <p class="claim claim--right">No Artificial Flavouring</p>
    <p class="center maker-name">VANTOOR</p>
    <h2 class="center gin-name">VANTOOR</h2>
    <p class="center gin-word">GIN</p>
    <p class="center premium">PREMIUM</p>
    <p class="center makers-line">DISTILLED AND BOTTLED BY VANTOOR DISTILLERY</p>
    <p class="center style-name">LONDON DRY GIN</p>
    <p class="center batch"><span>HANDCRAFTED IN SMALL BATCH</span></p>
    <div class="facts"><span>50 CL|43% ALC.</span><span class="origin-oval">PRODUCT OF<br>NETHERLANDS</span><span>VOL. 500 ML</span></div>
  </section>

  <section class="label label--wine">
    <svg class="frame" viewBox="0 0 542 400" preserveAspectRatio="none">
      <defs>
        <radialGradient id="wine-glow" cx="0.5" cy="0.35" r="0.7">
          <stop offset="0" stop-color="var(--rose)"/><stop offset=".6" stop-color="var(--wine)"/><stop offset="1" stop-color="#2a0818"/>
        </radialGradient>
      </defs>
      <polygon points="0,140 542,15 542,395 0,395" fill="url(#wine-glow)"/>
      <polyline points="24,380 24,152 518,40 518,380 24,380" fill="none" stroke="#d9b9c6" stroke-width="1"/>
      <path d="M24 322 H518" stroke="#d9b9c6" stroke-width="1"/>
    </svg>
    <svg class="badge" viewBox="0 0 340 220" aria-label="Vantoor Gin premium badge">
      <use href="#badge-art"/>
    </svg>
    <p class="center style-caps">LONDON DRY GIN</p>
    <p class="info-band">100% NATURAL BOTANICALS &#9679; NO ARTIFICIAL FLAVOURING<br>DISTILLED AND BOTTLED BY VANTOOR DISTILLERY</p>
    <div class="fact-row"><span>50 CL|43% ALC.</span><span>PRODUCT OF NETHERLANDS</span><span>VOL. 500 ML</span></div>
  </section>

  <svg width="0" height="0" style="position:absolute">
    <defs>
      <g id="badge-art">
        <circle cx="170" cy="108" r="106" fill="var(--cream)" stroke="var(--ink)" stroke-width="3"/>
        <circle cx="170" cy="108" r="99" fill="none" stroke="var(--ink)" stroke-width="1"/>
        <path d="M20 58 H320 Q320 70 334 70 V150 Q320 150 320 162 H20 Q20 150 6 150 V70 Q20 70 20 58 Z" fill="var(--cream)" stroke="var(--ink)" stroke-width="3"/>
        <path d="M26 64 H314 Q314 76 326 76 V144 Q314 144 314 156 H26 Q26 144 14 144 V76 Q26 76 26 64 Z" fill="none" stroke="var(--ink)" stroke-width="1"/>
        <text x="170" y="42" text-anchor="middle" font-family="Oswald, sans-serif" font-weight="600" font-size="22" letter-spacing="2" fill="var(--logo-red)">VANTOOR</text>
        <text x="170" y="134" text-anchor="middle" font-family="Oswald, sans-serif" font-weight="500" font-size="52" textLength="270" lengthAdjust="spacingAndGlyphs" fill="var(--ink)">VANTOOR GIN</text>
        <rect x="112" y="140" width="116" height="12" rx="6" fill="var(--ornament)" role="img" aria-label="Decorative scroll flourish"/>
        <text x="170" y="178" text-anchor="middle" font-family="Josefin Sans, sans-serif" font-weight="700" font-size="12" letter-spacing="1" fill="var(--ink)">PREMIUM</text>
        <path id="badge-arc" d="M102 170 A92 92 0 0 0 238 170" fill="none"/>
        <text font-family="Josefin Sans, sans-serif" font-weight="700" font-size="7.5" letter-spacing=".4" fill="var(--ink)"><textPath href="#badge-arc" startOffset="50%" text-anchor="middle">HANDCRAFTED IN SMALL BATCH</textPath></text>
      </g>
    </defs>
  </svg>

</main>
</body>
</html>
```